Rural contractor needs professional informative business card

We need a business card design that looks professional but also includes information about the services that the business offers.
The business is an earthmoving and transport business. All of the services offered are listed on the old card attached.
The business is aimed at farmers so the design we are after is a classic look. The card needs to include all of the information that is listed on the old card design uploaded as an attachment. We recognize that this is a lot of information to fit on a business card but it also operates as a key marketing tool so is very important to the business.
Feel free to send me your questions.
Thanks
Reason: We are having trouble deciding between all these great designs - thank you for your efforts
We would love to see some designs using red with a little white and black. Also feel free to re-design our logo if you feel it needs to be to fit your designs. Thank you

```html
<!DOCTYPE html>
<html lang="en">
<head>
<meta charset="utf-8">
<title>RT Harlow Contracting – Business Card</title>
<link rel="stylesheet" href="https://fonts.googleapis.com/css2?family=Source+Sans+3:wght@400;600;700&display=swap">
<style>
  :root {
    --red: #e8242b;
    --red-soft: #f2897d;
    --black: #111111;
    --white: #ffffff;
    --page: #3a3a3a;
    --ink: #1a1a1a;
  }
  * { box-sizing: border-box; margin: 0; padding: 0; }
  html, body { width: 1200px; height: 750px; overflow: hidden; }
  body {
    background: var(--page);
    font-family: "Source Sans 3", "Myriad Pro", Arial, sans-serif;
    position: relative;
  }
  .card {
    position: absolute;
    top: 229px;
    width: 510px;
    height: 292px;
    border-radius: 18px;
    overflow: hidden;
    background: var(--red);
    color: var(--ink);
  }
  .card--front { left: 78px; }
  .card--back { left: 610px; }

  /* Brand name block */
  .brand {
    position: absolute;
    font-weight: 700;
    line-height: 1;
    white-space: nowrap;
  }
  .brand__name { display: block; font-size: 36px; }
  .brand__line { display: block; font-size: 15px; letter-spacing: 6.4px; margin-top: 6px; padding-left: 4px; }
  .card--front .brand { left: 34px; top: 28px; color: var(--white); }

  /* Services */
  .service-group { position: absolute; }
  .service-group--transport { left: 29px; top: 100px; }
  .service-group--earthmoving { left: 353px; top: 58px; }
  .service-group h2 {
    font-size: 17px;
    font-weight: 400;
    line-height: 20px;
    color: var(--ink);
  }
  .service-list { list-style: none; }
  .service-list li {
    display: flex;
    align-items: center;
    gap: 9px;
    font-size: 16px;
    line-height: 17.5px;
    color: var(--white);
  }
  .service-list svg { width: 16px; height: 14px; flex: none; }
  .photo-haulage {
    position: absolute;
    left: 0; right: 0; bottom: 0;
    height: 125px;
    background: linear-gradient(180deg, rgba(232,36,43,0) 0%, rgba(120,120,112,0.7) 28%, #cfcfcb 50%, #3a3a3a 76%, #0d0d0d 100%);
  }

  /* Back */
  .contact { position: absolute; left: 26px; top: 31px; color: var(--ink); }
  .contact__name { font-size: 19px; font-weight: 400; line-height: 22px; }
  .contact__line {
    display: flex; align-items: center; gap: 9px;
    font-size: 16px; line-height: 17.5px;
  }
  .contact__line svg { width: 16px; height: 14px; flex: none; }
  .contact__line--indent { padding-left: 25px; }
  .monogram {
    position: absolute; left: 347px; top: 29px;
    width: 108px; height: 108px;
    border: 1.5px solid var(--red-soft);
    border-radius: 50%;
    display: flex; align-items: center; justify-content: center;
    font-size: 46px; font-weight: 400; letter-spacing: 8px; padding-left: 8px;
    color: var(--red-soft);
  }
  .tagline-band {
    position: absolute; left: 0; right: 0; top: 142px; height: 31px;
    background: var(--black);
    color: var(--white);
    font-size: 16px;
    line-height: 31px;
    padding-left: 26px;
  }
  .stripe { position: absolute; left: 0; right: 0; top: 173px; height: 16px; background: var(--red); }
  .white-panel { position: absolute; left: 0; right: 0; top: 189px; bottom: 0; background: var(--white); }
  .card--back .brand { left: 28px; top: 210px; color: var(--black); }
  .photo-loader {
    position: absolute; left: 330px; top: 150px; width: 176px; height: 142px;
    border-radius: 12px;
    background: radial-gradient(ellipse at 60% 55%, #f2b51c 0%, #d99a10 40%, #4a4a46 72%, rgba(255,255,255,0) 100%);
  }
</style>
</head>
<body>
  <section class="card card--front">
    <div class="photo-haulage" role="img" aria-label="Photo of a white prime mover truck hauling a long flatbed trailer loaded with equipment"></div>
    <p class="brand"><span class="brand__name">RT Harlow</span><span class="brand__line">CONTRACTING</span></p>

    <div class="service-group service-group--transport">
      <h2>Transport</h2>
      <ul class="service-list">
        <li><svg viewBox="0 0 16 14"><path d="M1 1h11v12H1z" fill="none" stroke="#111" stroke-width="1.6"/><path d="M3 7l3 3 8-9" fill="none" stroke="#111" stroke-width="2.6"/></svg>Road building &amp; maintenance</li>
        <li><svg viewBox="0 0 16 14"><path d="M1 1h11v12H1z" fill="none" stroke="#111" stroke-width="1.6"/><path d="M3 7l3 3 8-9" fill="none" stroke="#111" stroke-width="2.6"/></svg>polu pipe laying</li>
        <li><svg viewBox="0 0 16 14"><path d="M1 1h11v12H1z" fill="none" stroke="#111" stroke-width="1.6"/><path d="M3 7l3 3 8-9" fill="none" stroke="#111" stroke-width="2.6"/></svg>Clearing fence lines</li>
        <li><svg viewBox="0 0 16 14"><path d="M1 1h11v12H1z" fill="none" stroke="#111" stroke-width="1.6"/><path d="M3 7l3 3 8-9" fill="none" stroke="#111" stroke-width="2.6"/></svg>Sand &amp; gravel supplies</li>
      </ul>
    </div>

    <div class="service-group service-group--earthmoving">
      <h2>Earthmoving</h2>
      <ul class="service-list">
        <li><svg viewBox="0 0 16 14"><path d="M1 1h11v12H1z" fill="none" stroke="#111" stroke-width="1.6"/><path d="M3 7l3 3 8-9" fill="none" stroke="#111" stroke-width="2.6"/></svg>Grain</li>
        <li><svg viewBox="0 0 16 14"><path d="M1 1h11v12H1z" fill="none" stroke="#111" stroke-width="1.6"/><path d="M3 7l3 3 8-9" fill="none" stroke="#111" stroke-width="2.6"/></svg>cotton</li>
        <li><svg viewBox="0 0 16 14"><path d="M1 1h11v12H1z" fill="none" stroke="#111" stroke-width="1.6"/><path d="M3 7l3 3 8-9" fill="none" stroke="#111" stroke-width="2.6"/></svg>Wool</li>
        <li><svg viewBox="0 0 16 14"><path d="M1 1h11v12H1z" fill="none" stroke="#111" stroke-width="1.6"/><path d="M3 7l3 3 8-9" fill="none" stroke="#111" stroke-width="2.6"/></svg>Sand &amp; gravel</li>
      </ul>
    </div>
  </section>

  <section class="card card--back">
    <div class="contact">
      <p class="contact__name">Rory Harlow</p>
      <p class="contact__line"><svg viewBox="0 0 16 14"><path d="M1 5c0-3 3-4 7-4s7 1 7 4l-3 1-1-2H5L4 6z" fill="#111"/><path d="M3 7h10l1 6H2z" fill="#111"/><circle cx="8" cy="10" r="1.6" fill="#e8242b"/></svg>0400 217 386</p>
      <p class="contact__line"><svg viewBox="0 0 16 14"><path d="M8 0a4.5 4.5 0 0 0-4.5 4.5C3.5 8 8 14 8 14s4.5-6 4.5-9.5A4.5 4.5 0 0 0 8 0z" fill="#111"/><circle cx="8" cy="4.6" r="1.7" fill="#e8242b"/></svg>27 Wattle Street</p>
      <p class="contact__line contact__line--indent">Dunmore 2830</p>
      <p class="contact__line"><svg viewBox="0 0 16 14"><rect x="3" y="4" width="10" height="7" fill="#111"/><path d="M3 4l5 4 5-4" fill="none" stroke="#e8242b" stroke-width="1"/></svg>rory@harlowmail.com</p>
    </div>
    <div class="monogram">RH</div>

    <div class="tagline-band">EARTHMOVING &amp; TRANSPORT SOLUTIONS</div>
    <div class="stripe"></div>
    <div class="white-panel"></div>
    <div class="photo-loader" role="img" aria-label="Photo of a yellow front-end wheel loader with a black bucket"></div>
    <p class="brand"><span class="brand__name">RT Harlow</span><span class="brand__line">CONTRACTING</span></p>
  </section>
</body>
</html>
```